Business Card for IT Support Company
Aide Nova
Business Card for IT Support Company - Information Technology
Creative Brief
Professional
Assistance Informatique 24/7
Tél. 0900 417 536
2.50 CHF/min de 8h à 22h et 3.50 CHF/min de 22h à 8h depuis le réseau fixe.
info@aide-nova.ch
http://www.aide-nova.ch
No specific name, this is only a hotline IT support number Business Card (phone number is in the title) in Address box, it's the rates on the Business Number. We will use brivopress . ch as the printing company, here are the exact size in mm they send to me: Business card Size is 85x55mm (But file dimension must be 91x61mm) Colors needs to be send in CMYK, minimum 200 dpi, maximum quality.
- Contrôle à distance PC/MAC - Support technique informatique - Formation / Consulting / Coaching - Infographie / Graphisme - Création de Site Web - Smartphone / Tablette

```html
<!DOCTYPE html>
<html lang="fr">
<head>
<meta charset="utf-8">
<title>Aide Nova – Carte de visite</title>
<link rel="stylesheet" href="https://fonts.googleapis.com/css2?family=Arimo:wght@700&family=Michroma&display=swap">
<style>
  :root {
    --backdrop: #e4e4e4;
    --card-white: #f4f4f4;
    --card-grey: #d9d9d9;
    --card-black: #0d0d0d;
    --accent-red: #d3141c;
    --text-dark: #3a3a3a;
    --text-light: #ffffff;
  }
  html, body {
    margin: 0;
    width: 1200px;
    height: 901px;
    overflow: hidden;
    background: var(--backdrop);
  }
  .business-card {
    position: absolute;
    left: 100px;
    top: 115px;
    width: 1000px;
    height: 670px;
    border-radius: 48px;
    overflow: hidden;
    background: var(--card-black);
    box-shadow: 0 10px 30px rgba(0,0,0,0.18);
  }
  .card-shapes {
    position: absolute;
    inset: 0;
    width: 100%;
    height: 100%;
  }
  .brand {
    position: absolute;
    left: 80px;
    top: 118px;
    display: flex;
    align-items: flex-start;
    gap: 22px;
  }
  .brand-dot {
    flex: none;
    width: 96px;
    height: 96px;
    border-radius: 50%;
    background: var(--accent-red);
  }
  .brand-name {
    font-family: "Arimo", Arial, sans-serif;
    font-weight: 700;
    font-size: 50px;
    line-height: 1;
    color: var(--text-dark);
    margin-top: 86px;
    white-space: nowrap;
  }
  .call-block {
    position: absolute;
    left: 585px;
    top: 405px;
    font-family: "Michroma", sans-serif;
    white-space: nowrap;
  }
  .call-label {
    color: var(--accent-red);
    font-size: 26px;
    letter-spacing: 2px;
    line-height: 1.2;
    margin: 0 0 10px;
  }
  .call-number {
    color: var(--text-light);
    font-size: 32px;
    letter-spacing: 2px;
    line-height: 1.2;
    margin: 0;
  }
  .contact-list {
    position: absolute;
    left: 80px;
    top: 525px;
    margin: 0;
    padding: 0;
    list-style: none;
    font-family: "Michroma", sans-serif;
    font-size: 22px;
    letter-spacing: 1px;
    color: var(--text-light);
    line-height: 1.75;
    white-space: nowrap;
  }
</style>
</head>
<body>
  <section class="business-card" aria-label="Carte de visite Aide Nova">
    <svg class="card-shapes" viewBox="0 0 1000 670" aria-hidden="true">
      <defs>
        <linearGradient id="card-face" x1="0" y1="0" x2="1" y2="1">
          <stop offset="0" stop-color="#f4f4f4"/>
          <stop offset="1" stop-color="#d9d9d9"/>
        </linearGradient>
      </defs>
      <path class="white-face" d="M0 0 H1000 V95 C760 190 560 300 380 370 C230 425 110 420 0 385 Z" fill="url(#card-face)"/>
      <path class="red-swoosh" d="M0 400 C130 445 250 440 390 390 C560 330 760 220 1000 120 L1000 138 C770 240 570 355 400 412 C250 462 130 462 0 420 Z" fill="#d3141c"/>
      <path class="grey-line" d="M0 440 C140 480 270 470 410 425 C580 370 780 260 1000 160" fill="none" stroke="#8a8a8a" stroke-width="3"/>
    </svg>

    <div class="brand">
      <span class="brand-dot"></span>
      <span class="brand-name">Aide Nova</span>
    </div>

    <div class="call-block">
      <p class="call-label">CALL US TODAY</p>
      <p class="call-number">0900 417 536</p>
    </div>

    <ul class="contact-list">
      <li>INFO@AIDE-NOVA.CH</li>
      <li>WWW.AIDE-NOVA.CH</li>
    </ul>
  </section>
</body>
</html>
```